High End Skincare for Women Cosmetics Brand

We need a wordpress website that is also a mobile-friendly website for our cosmetics company. We have 3 core products and have 10 dropship products to add. I have attached the pdf with brand guide and vision for the website.

Our mission - At Mira Vale we believe all women have four distinct characteristics; beauty, originality, passion, and confidence. Our beauty products simply enhance those qualities. We will always provide the safest products to our consumers and continue to uplift women around the world.

About us - MIRA VALE IS AN ORGANIC COSMETICS AND SKINCARE BRAND WITH VARIOUS PRODUCTS TO ENHANCE YOUR NATURAL BEAUTY. WE ARE COMMITTED TO PROVIDING TIMELESS PRODUCTS THAT WILL BRING OUT THAT SPECIAL CONFIDENCE YOU FEEL AND DESIRE FROM COSMETICS THAT WILL PERFECTLY MESH YOUR LIFESTYLE. When you choose Mira Vale organic cosmetics and skincare products, you are choosing a product whose ingredients work perfectly with the most complicated natural skin. We want you to celebrate that unique natural beauty with Mira Vale organic cosmetics and skincare products that will enhance your beauty. We use the best quality plant-based and laboratory-made ingredients to produce the best organic products that will enhance your beauty and boost your confidence.

XoXo Mira Vale - We understand that beauty is much more than an outward appearance. Our unique products bring you confidence, courage, and enrich your spirit. True beauty is deeper, and we at Mira Vale seek to inspire you to discover that deep sense of beauty you always craved.

Style - Luxury High End / Should look expensive and feminine with a modern touch.
The logo files are attached to this.

Colors should be bold and bright that looks like luxury and modern.

The products we sell are organic skincare and cosmetic products.

The design should not include any images or generic types of a font that can be found in Microsoft Word.

Premium font required.

Mira Vale is a leading organic cosmetics and skincare brand with products that enhance the natural beauty of the everyday woman. Luxury without the luxe price tag.

Target Market(s)

Target audience women age 18- 42 Gen Y / Millennials / Gen X

Industry/Entity Type

Beauty

Number of Pages Required

4 page

Font styles to use
Sans Serif

Colors

Designer to choose colors to be used in the design.

Requirements
Must have
• Must have images of women of diverse ethnicity at least 4 women
• Must have images of products -
• Must have an option to integrate dropship product links
• Must have contact us form
• Must have about us page
• Must have high-resolution images
• Must have a feature to check out on the website
• Must be mobile friendly
Nice to have
• Nice to have blog feature
• Nice to have a chat bot

```html
<!DOCTYPE html>
<html lang="en">
<head>
<meta charset="utf-8">
<title>Mira Vale — Organic Cosmetics &amp; Skincare</title>
<link rel="stylesheet" href="https://fonts.googleapis.com/css2?family=Montserrat:wght@200;300;400;500;600;700&family=Open+Sans:wght@400;600&display=swap">
<style>
:root{
  --pink:#ec8c9e;
  --pink-soft:#f6c7cf;
  --cream:#fdf6e6;
  --ink:#222222;
  --body:#555555;
  --grey-band:#f1f1f1;
  --line:#dddddd;
  --footer:#121212;
  --footer-text:#9a9a9a;
  --white:#ffffff;
}
*{margin:0;padding:0;box-sizing:border-box}
html,body{width:1200px;height:4444px;overflow:hidden}
body{position:relative;background:var(--white);font-family:"Open Sans",sans-serif;color:var(--ink)}
.abs{position:absolute}
.photo{position:absolute}
h2.section-title{position:absolute;font-family:"Montserrat",sans-serif;font-weight:600;font-size:29px;letter-spacing:1px;color:var(--ink)}
.rule{position:absolute;height:3px;width:70px;background:var(--pink)}
p.copy{position:absolute;font-size:12.5px;line-height:20px;color:var(--body)}

/* header & hero */
.hero{left:0;top:0;width:1200px;height:630px;background:var(--cream);overflow:hidden}
.hero-model{left:0;top:0;width:450px;height:630px;background:linear-gradient(160deg,#e9d6c6,#c9a28c 55%,#f3e6d8)}
.hero-bloom-top{right:0;top:120px;width:210px;height:230px;border-radius:50% 0 0 50%;background:radial-gradient(circle at 60% 50%,#f3a093,#f9d1c5 70%,transparent 71%)}
.hero-bloom-leaf{right:0;top:470px;width:120px;height:160px;border-radius:60% 0 0 40%;background:radial-gradient(circle at 70% 50%,#c9b56b,#e5d9a1 70%,transparent 71%)}
.hero-bloom-low{left:730px;top:470px;width:240px;height:160px;border-radius:50% 50% 0 0;background:radial-gradient(circle at 50% 80%,#f3b3a8,#fbe1d9 65%,transparent 66%)}
.brand{font-family:"Montserrat",sans-serif;font-weight:300;letter-spacing:10px;color:var(--ink)}
.header-brand{left:170px;top:36px;font-size:27px}
.nav{left:470px;top:42px;display:flex;gap:34px;font-family:"Montserrat",sans-serif;font-size:12px;font-weight:600;letter-spacing:.5px}
.nav span.active{border-bottom:2px solid var(--ink);padding-bottom:3px}
.nav-icon{top:34px;width:30px;height:30px;border:1.5px solid var(--ink);border-radius:50%}
.hero-welcome{left:0;width:1480px;top:238px;text-align:center;font-family:"Montserrat",sans-serif;font-weight:400;font-size:31px;letter-spacing:4px}
.hero-brand{left:0;width:1480px;top:282px;text-align:center;font-size:70px;font-weight:200;letter-spacing:14px}
.btn-pill{position:absolute;border-radius:20px;background:var(--pink);color:var(--white);font-family:"Montserrat",sans-serif;font-weight:600;font-size:11px;letter-spacing:1px;text-align:center}
.hero-btn{left:695px;top:385px;width:125px;height:32px;line-height:32px}
.dots{left:528px;top:592px;display:flex;gap:6px}
.dots i{display:block;width:33px;height:4px;background:#555}
.dots i.on{background:var(--ink)}

/* about & mission */
.frame{position:absolute;border:10px solid var(--pink-soft)}
.sub-pink{position:absolute;font-family:"Montserrat",sans-serif;font-size:15px;line-height:22px;color:var(--pink);letter-spacing:.5px}

/* products */
.products{left:0;top:1770px;width:1200px;height:1030px;background:var(--grey-band)}
.card{position:absolute;width:270px;height:352px;background:var(--white);border:1px solid #e6e6e6;text-align:center}
.card .shot{position:absolute;left:65px;top:25px;width:140px;height:150px;border-radius:4px}
.card .price{position:absolute;left:0;width:100%;top:205px;font-size:17px;color:var(--pink)}
.card .name{position:absolute;left:0;width:100%;top:235px;font-family:"Montserrat",sans-serif;font-size:16px;font-weight:500;letter-spacing:.5px}
.card .buy{position:absolute;left:85px;top:283px;width:100px;height:28px;line-height:26px;border:1px solid #999;border-radius:14px;font-size:10.5px;font-weight:600;letter-spacing:1px}

/* blog */
.blog-title{position:absolute;font-family:"Montserrat",sans-serif;font-weight:600;font-size:17px;line-height:23px;letter-spacing:.5px}
.blog-date{position:absolute;font-size:11px;color:var(--pink)}

/* contact */
.field{position:absolute;left:172px;width:378px;height:34px;border:1px solid #cfcfcf;background:var(--white);font-size:12px;padding:9px 10px;color:#333}

/* footer */
.footer{left:0;top:4040px;width:1200px;height:404px;background:var(--footer);color:var(--white)}
.footer h4{position:absolute;font-family:"Montserrat",sans-serif;font-weight:500;font-size:15px}
.footer ul{position:absolute;list-style:none;font-size:11px;line-height:22px;color:var(--footer-text)}
.social{position:absolute;top:4090px;width:22px;height:22px;border-radius:50%;background:var(--pink)}
</style>
</head>
<body>

<!-- Hero -->
<section class="abs hero">
  <div class="photo hero-model" role="img" aria-label="Woman with dark hair holding a skincare jar on her open hand"></div>
  <div class="photo hero-bloom-top" role="img" aria-label="Coral flower"></div>
  <div class="photo hero-bloom-leaf" role="img" aria-label="Yellow green leaf"></div>
  <div class="photo hero-bloom-low" role="img" aria-label="Pale pink paper flower"></div>
  <div class="abs brand header-brand">MIRA VALE</div>
  <nav class="abs nav"><span class="active">HOME</span><span>ABOUT US</span><span>PRODUCTS ▾</span><span>NEWS</span><span>CONTACT US</span></nav>
  <svg class="abs nav-icon" style="left:955px" viewBox="0 0 30 30"><circle cx="13.5" cy="13.5" r="5" fill="none" stroke="#222" stroke-width="1.6"/><line x1="17" y1="17" x2="21" y2="21" stroke="#222" stroke-width="1.6"/></svg>
  <svg class="abs nav-icon" style="left:993px" viewBox="0 0 30 30"><path d="M8 10h2l2 8h8l2-6H11" fill="none" stroke="#222" stroke-width="1.5"/><circle cx="13" cy="21" r="1.2" fill="#222"/><circle cx="19" cy="21" r="1.2" fill="#222"/></svg>
  <div class="abs hero-welcome">WELCOME TO</div>
  <div class="abs brand hero-brand">MIRA VALE</div>
  <div class="btn-pill hero-btn">READ MORE</div>
  <div class="abs dots"><i></i><i class="on"></i><i></i><i></i></div>
</section>

<!-- About -->
<section>
  <div class="frame" style="left:160px;top:780px;width:412px;height:362px"></div>
  <div class="photo" style="left:172px;top:780px;width:390px;height:350px;background:linear-gradient(150deg,#b98a6c,#6b4534 60%,#d8c3b5)" role="img" aria-label="Portrait of a woman with curly hair"></div>
  <h2 class="section-title" style="left:605px;top:803px">ABOUT MIRA VALE</h2>
  <div class="rule" style="left:605px;top:848px"></div>
  <p class="copy" style="left:605px;top:872px;width:420px">Mira Vale is an organic cosmetics and skincare brand with various products to enhance your natural beauty. We are committed to providing timeless products that will bring out that special confidence you feel and desire from cosmetics that will perfectly mesh your lifestyle.</p>
  <p class="copy" style="left:605px;top:978px;width:420px">When you choose Mira Vale organic cosmetics and skincare products, you are choosing a product whose ingredients work perfectly with the most complicated natural skin. We want you to celebrate that unique natural beauty with Mira Vale organic cosmetics and skincare products that will enhance your beauty. We use the best quality plant-based and laboratory-made ingredients to produce the best organic products that will enhance your beauty and boost your confidence.</p>
</section>

<!-- Mission -->
<section>
  <h2 class="section-title" style="left:172px;top:1298px">OUR MISSION</h2>
  <div class="rule" style="left:172px;top:1343px"></div>
  <div class="sub-pink" style="left:172px;top:1374px;width:340px">ENHANCE THE INNER BEAUTY WOMEN AROUND THE WORLD!</div>
  <p class="copy" style="left:172px;top:1440px;width:420px">Our mission as a reputable organic cosmetics and skincare brand is to enhance your life with more enrichment and beauty. We understand that beauty is much more than an outward appearance. Our unique products bring you confidence, courage, and enrich your spirit. True beauty is deeper, and we at Mira Vale seek to inspire you to discover that deep sense of beauty you always craved.</p>
  <div class="frame" style="left:632px;top:1305px;width:410px;height:290px"></div>
  <div class="photo" style="left:642px;top:1230px;width:388px;height:355px;background:linear-gradient(135deg,#fafafa,#e8e4e2 50%,#cfc9c6)" role="img" aria-label="Flat lay of makeup brushes, compacts and lipsticks on white"></div>
  <div class="photo" style="left:985px;top:1560px;width:215px;height:190px;border-radius:50%;background:radial-gradient(circle,#f4c3b6,#fbe3dc 60%,transparent 70%)" role="img" aria-label="Pale pink paper flower"></div>
</section>

<!-- Products -->
<section class="abs products">
  <div class="photo" style="left:90px;top:500px;width:200px;height:200px;border-radius:50%;background:radial-gradient(circle,#f6c9ba,#fbe6de 60%,transparent 70%)" role="img" aria-label="Pale pink paper flower"></div>
  <h2 class="section-title" style="left:0;width:1200px;text-align:center;top:55px">OUR PRODUCTS</h2>
  <div class="rule" style="left:565px;top:100px"></div>

  <div class="card" style="left:172px;top:145px"><div class="shot" role="img" aria-label="Black skincare jar" style="background:linear-gradient(#fff,#e9e9e9)"></div><div class="price">$39.00</div><div class="name">MIRA VALE MASK</div><div class="buy">BUY NOW</div></div>
  <div class="card" style="left:465px;top:145px"><div class="shot" role="img" aria-label="Black pump bottle of cleanser" style="background:linear-gradient(#fff,#e9e9e9)"></div><div class="price">$39.00</div><div class="name">CLEANSER</div><div class="buy">BUY NOW</div></div>
  <div class="card" style="left:757px;top:145px"><div class="shot" role="img" aria-label="Eyeliner pencil and pot" style="background:linear-gradient(#fff,#e9e9e9)"></div><div class="price">$39.00</div><div class="name">PRODUCT NAME</div><div class="buy">BUY NOW</div></div>
  <div class="card" style="left:172px;top:520px"><div class="shot" role="img" aria-label="Mascara tube and wand" style="background:linear-gradient(#fff,#ecdcd8)"></div><div class="price">$39.00</div><div class="name">PRODUCT NAME</div><div class="buy">BUY NOW</div></div>
  <div class="card" style="left:465px;top:520px"><div class="shot" role="img" aria-label="Row of pink and red lipsticks" style="background:linear-gradient(#fff,#e6c2c6)"></div><div class="price">$39.00</div><div class="name">MIRA VALE LIPCARE</div><div class="buy">BUY NOW</div></div>
  <div class="card" style="left:757px;top:520px"><div class="shot" role="img" aria-label="Eyeshadow palette in rose tones" style="background:linear-gradient(#2a2a2a,#8a5a5a)"></div><div class="price">$39.00</div><div class="name">FACEMAKEUP</div><div class="buy">BUY NOW</div></div>

  <div class="btn-pill" style="left:483px;top:940px;width:234px;height:34px;line-height:34px">VIEW MORE PRODUCTS</div>
</section>

<!-- Blog -->
<section>
  <h2 class="section-title" style="left:0;width:1200px;text-align:center;top:2900px">LATEST BLOG</h2>
  <div class="rule" style="left:565px;top:2945px"></div>
  <div class="photo" style="left:172px;top:3000px;width:415px;height:275px;background:linear-gradient(120deg,#d9d9d9,#6d4a3a 55%,#cfcfcf)" role="img" aria-label="Woman with sleek ponytail in profile"></div>
  <div class="blog-title" style="left:172px;top:3295px">AWAKEN YOUR INHERENT BEAUTY</div>
  <p class="copy" style="left:172px;top:3325px;width:400px;font-size:11px;line-height:17px">Sed ut perspiciatis unde omnis iste natus error sit voluptatem accusantium doloremque laudantium, totam rem aperiam, eaque ipsa.</p>
  <div class="blog-date" style="left:172px;top:3380px">APR 08 2019</div>

  <div class="photo" style="left:605px;top:3000px;width:205px;height:185px;background:linear-gradient(135deg,#c9a98a,#e7c9b2 55%,#f1e0d3)" role="img" aria-label="Skincare bottles with dried petals"></div>
  <div class="blog-title" style="left:826px;top:3018px;width:200px">FROM THE HEART OF MIRA VALE</div>
  <p class="copy" style="left:826px;top:3070px;width:200px;font-size:11px;line-height:16px">Sed ut perspiciatis unde omnis iste natus error sit voluptatem accusantium doloremque laudantium, totam rem aperiam, eaque ipsa.</p>
  <div class="blog-date" style="left:826px;top:3150px">APR 08 2019</div>

  <div class="photo" style="left:605px;top:3205px;width:205px;height:185px;background:linear-gradient(135deg,#f4d2d6,#e8b9a3 55%,#f7e6e4)" role="img" aria-label="Blonde woman among pink flowers"></div>
  <div class="blog-title" style="left:826px;top:3222px;width:200px">ENHANCE THE INNER BEAUTY WOMEN</div>
  <p class="copy" style="left:826px;top:3274px;width:200px;font-size:11px;line-height:16px">Sed ut perspiciatis unde omnis iste natus error sit voluptatem accusantium doloremque laudantium, totam rem aperiam, eaque ipsa.</p>
  <div class="blog-date" style="left:826px;top:3355px">APR 08 2019</div>
</section>

<!-- Contact -->
<section>
  <div class="abs" style="left:0;top:3540px;width:600px;height:500px;background:#f8f5f3"></div>
  <div class="photo" style="left:0;top:3790px;width:230px;height:240px;border-radius:0 50% 50% 0;background:radial-gradient(circle at 30% 50%,#f0d5cd,#f7ebe6 60%,transparent 70%)" role="img" aria-label="Faint pink flowers and leaves"></div>
  <div class="photo" style="left:600px;top:3540px;width:600px;height:500px;background:linear-gradient(120deg,#f6c4b4,#e9a995 50%,#f3d1c4)" role="img" aria-label="Woman with hands framing her face on a peach background"></div>
  <h2 class="section-title" style="left:172px;top:3620px">CONTACT US</h2>
  <div class="rule" style="left:172px;top:3663px"></div>
  <div class="field" style="top:3700px">Name:</div>
  <div class="field" style="top:3740px">Email:</div>
  <div class="field" style="top:3780px">Phone:</div>
  <div class="field" style="top:3820px;height:118px">Comments:</div>
  <div class="btn-pill" style="left:172px;top:3952px;width:86px;height:30px;line-height:30px">SUBMIT</div>
</section>

<!-- Footer -->
<footer class="abs footer">
  <div class="abs brand" style="left:172px;top:42px;font-size:27px;color:#fff">MIRA VALE</div>
  <h4 style="left:172px;top:125px">Contact</h4>
  <svg class="abs" style="left:172px;top:160px" width="18" height="22" viewBox="0 0 18 22"><path d="M9 1a7 7 0 0 0-7 7c0 5 7 13 7 13s7-8 7-13a7 7 0 0 0-7-7z" fill="none" stroke="#bbb" stroke-width="1.4"/><circle cx="9" cy="8" r="2.5" fill="none" stroke="#bbb" stroke-width="1.4"/></svg>
  <ul style="left:210px;top:160px"><li>210 Rosewood Avenue</li><li>Fairview, CA 90210</li></ul>
  <svg class="abs" style="left:172px;top:222px" width="20" height="20" viewBox="0 0 20 20"><path d="M4 2l3 0 2 5-2 1.5a11 11 0 0 0 4.5 4.5L13 11l5 2v3a2 2 0 0 1-2 2A15 15 0 0 1 2 4a2 2 0 0 1 2-2z" fill="none" stroke="#bbb" stroke-width="1.4"/></svg>
  <ul style="left:210px;top:218px"><li>1-800-555-0142</li><li>1-800-555-0187</li></ul>
  <svg class="abs" style="left:172px;top:282px" width="22" height="16" viewBox="0 0 22 16"><rect x="1" y="1" width="20" height="14" fill="none" stroke="#bbb" stroke-width="1.4"/><path d="M1 1l10 8 10-8" fill="none" stroke="#bbb" stroke-width="1.4"/></svg>
  <ul style="left:210px;top:276px"><li>hello@miravale.com</li><li>care@miravale.com</li></ul>

  <h4 style="left:437px;top:125px">Products</h4>
  <ul style="left:437px;top:158px"><li>Lorem ipsum dolor</li><li>Consectetur adipiscing elit</li><li>Sed do eiusmod</li><li>Tempor incididunt</li><li>Ut labore dolore</li><li>Magna aliqua</li></ul>
  <h4 style="left:653px;top:125px">Account</h4>
  <ul style="left:653px;top:158px"><li>Lorem ipsum dolor</li><li>Consectetur adipiscing elit</li><li>Sed do eiusmod</li><li>Tempor incididunt</li><li>Ut labore dolore</li><li>Magna aliqua</li></ul>
  <h4 style="left:884px;top:125px">Other Links</h4>
  <ul style="left:884px;top:158px"><li>Lorem ipsum</li><li>Dolor sit amet</li><li>Sed do eiusmod</li><li>Tempor incididunt</li><li>Ut labore dolore</li><li>Magna aliqua</li></ul>

  <div class="photo" style="left:0;top:260px;width:150px;height:144px;border-radius:0 50% 0 0;background:radial-gradient(circle at 30% 70%,#f6cfc2,#fbe7e0 55%,transparent 70%)" role="img" aria-label="Pale pink paper flower"></div>
  <div class="abs" style="left:172px;top:358px;font-size:11px;color:#ddd">Copyright 2019 All Rights Reserved</div>
  <div class="btn-pill" style="left:930px;top:352px;width:96px;height:26px;line-height:26px;font-size:10px">CHAT NOW</div>
</footer>
<div class="social" style="left:940px"></div>
<div class="social" style="left:970px"></div>
<div class="social" style="left:1000px"></div>

</body>
</html>
```